Webpage

I am a professional genealogist. I need a webpage that is professional looking (using the logo I chose), I can add hyperlinks and photos to if and when I want.

```html
<!DOCTYPE html>
<html lang="en">
<head>
<meta charset="utf-8">
<title>Dana Whitfield – Professional Genealogist</title>
<link href="https://fonts.googleapis.com/css2?family=Open+Sans:wght@400;600;700&family=Raleway:wght@600;700;800&display=swap" rel="stylesheet">
<style>
:root{
  --teal:#6cbf9c;
  --teal-dark:#4fa583;
  --ink:#333a40;
  --muted:#8a9196;
  --light:#f2f3f3;
  --band:#e9eaea;
  --dark:#2e3033;
  --darker:#232527;
  --white:#ffffff;
  --photo-a:#b9cdd6;
  --photo-b:#dfe8ec;
}
*{box-sizing:border-box;margin:0;padding:0}
html,body{width:1200px;height:3212px;overflow:hidden}
body{font-family:"Open Sans",Arial,sans-serif;color:var(--ink);background:var(--white);position:relative}
a{color:inherit;text-decoration:none}
.section-title{font-family:"Raleway",Arial,sans-serif;font-weight:800;font-size:30px;text-align:center;letter-spacing:1px;text-transform:uppercase;color:var(--ink)}
.section-rule{width:60px;height:3px;background:var(--teal);margin:14px auto 0}
.photo{background:linear-gradient(135deg,var(--photo-b),var(--photo-a))}

/* top bar */
.topbar{height:36px;background:var(--teal);display:flex;align-items:center;padding-left:130px;color:var(--white);font-size:13px;gap:44px}
.topbar span{display:flex;align-items:center;gap:8px}
.topbar .cta{margin-left:auto;background:var(--dark);height:36px;width:220px;display:flex;align-items:center;justify-content:center;font-weight:600;letter-spacing:.5px;text-transform:uppercase;font-size:12px}

/* header */
.header{height:80px;display:flex;align-items:center;padding:0 130px}
.brand{display:flex;align-items:center;gap:12px}
.brand-mark{width:44px;height:44px;border-radius:50%;background:var(--teal)}
.brand-name{font-weight:600;font-size:20px;color:var(--ink)}
.nav{margin-left:auto;display:flex;gap:26px;font-size:14px;font-weight:600;text-transform:uppercase}
.nav a.active{color:var(--teal)}

/* hero */
.hero{height:512px;position:relative;background:linear-gradient(120deg,#c9d8dc 0%,#e8eef0 45%,#b7c8cf 100%)}
.hero-box{position:absolute;left:130px;top:60px;width:390px;background:rgba(108,191,156,.88);color:var(--white);padding:26px 28px 30px}
.hero-box h1{font-family:"Raleway",Arial,sans-serif;font-weight:800;font-size:38px;line-height:1.05;text-transform:uppercase}
.hero-box h2{font-family:"Raleway",Arial,sans-serif;font-weight:700;font-size:22px;text-transform:uppercase;margin-top:6px}
.hero-box p{font-size:14px;line-height:1.5;margin-top:14px}
.hero-btn{display:inline-block;margin-top:20px;background:var(--dark);padding:10px 20px;font-size:12px;text-transform:uppercase}

/* services */
.services{height:432px;padding-top:72px;position:relative}
.service-list{display:flex;justify-content:center;gap:60px;margin-top:62px}
.service{width:280px;text-align:center}
.service-icon{width:84px;height:84px;border-radius:50%;background:var(--teal);margin:0 auto;display:flex;align-items:center;justify-content:center}
.service h3{font-size:15px;font-weight:700;text-transform:uppercase;margin-top:22px}
.service p{font-size:12px;color:var(--muted);line-height:1.6;margin-top:10px}
.arrow{position:absolute;width:22px;height:22px;border-radius:50%;background:#c8cccf;display:flex;align-items:center;justify-content:center}

/* work */
.work{height:460px;padding-top:28px;border-top:1px solid #e4e6e7}
.work-grid{display:grid;grid-template-columns:repeat(6,155px);grid-template-rows:158px 158px;gap:0;margin:50px auto 0;width:930px}
.work-feature{grid-column:1/3;grid-row:2;background:var(--teal);color:var(--white);padding:34px 30px}
.work-feature h4{font-size:15px;font-weight:700;text-transform:uppercase}
.work-feature a{display:block;margin-top:18px;font-size:12px}
.tile-wide{grid-column:span 2}

/* why */
.why{height:392px;background:var(--band);padding-top:52px;border-top:1px solid #dcdfe0}
.why-grid{width:930px;margin:44px auto 0;display:grid;grid-template-columns:repeat(3,1fr);row-gap:44px;column-gap:40px}
.why-item{display:flex;gap:14px}
.why-num{flex:0 0 24px;height:24px;border-radius:50%;background:var(--teal);color:var(--white);font-size:12px;font-weight:700;display:flex;align-items:center;justify-content:center}
.why-item h5{font-size:13px;font-weight:700;text-transform:uppercase}
.why-item p{font-size:12px;color:var(--muted);line-height:1.6;margin-top:6px}

/* team */
.team{height:700px;padding-top:120px}
.team-list{display:flex;justify-content:center;gap:100px;margin-top:34px}
.member{width:256px}
.member .photo{height:320px}
.member-row{display:flex;justify-content:space-between;align-items:flex-start;margin-top:22px}
.member h6{font-size:14px;font-weight:700;text-transform:uppercase}
.member small{display:block;font-size:13px;color:var(--muted);margin-top:6px}
.dots{display:flex;gap:6px;margin-top:14px}
.dots i{width:18px;height:18px;border-radius:50%;background:var(--teal);display:block}

/* partners */
.partners{height:200px;border-top:1px solid #e4e6e7;position:relative}
.partner-list{position:absolute;left:190px;right:190px;top:0;bottom:0;display:flex;align-items:center;justify-content:space-between}
.partner{font-weight:700;font-size:20px;color:#555b60;display:flex;align-items:center;gap:8px;white-space:nowrap}
.partner b{width:14px;height:14px;background:#555b60;display:block}

/* footer */
.footer{height:320px;background:var(--dark);color:#c8cbce;padding:48px 130px 0;display:grid;grid-template-columns:200px 220px 230px 1fr;gap:40px}
.footer h6{color:var(--white);font-size:13px;font-weight:700;text-transform:uppercase;margin-bottom:14px}
.footer p{font-size:12px;line-height:1.7}
.footer .more{display:inline-block;margin-top:14px;font-size:12px;color:var(--white)}
.tweet{display:flex;gap:8px;font-size:12px;margin-bottom:12px;background:#383b3e;padding:6px 8px}
.tweet i{flex:0 0 12px;height:12px;border-radius:50%;background:var(--teal);margin-top:2px}
.subscribe{display:flex;margin-top:16px}
.subscribe span{flex:1;background:var(--white);color:var(--muted);font-size:12px;padding:9px 12px;white-space:nowrap}
.subscribe b{background:var(--teal);color:var(--white);font-size:12px;padding:9px 18px}
.bottom{height:80px;background:var(--darker);color:#9ea3a7;font-size:12px;display:flex;align-items:center;padding:0 130px;gap:28px}
.bottom .copy{margin-right:auto}
.bottom .social{display:flex;gap:8px}
.bottom .social i{width:20px;height:20px;border-radius:50%;background:#55595d;display:block}
</style>
</head>
<body>

<div class="topbar">
  <span><svg width="12" height="12" viewBox="0 0 24 24"><path fill="#fff" d="M6.6 10.8a15.5 15.5 0 0 0 6.6 6.6l2.2-2.2a1 1 0 0 1 1-.25 11.4 11.4 0 0 0 3.6.6 1 1 0 0 1 1 1V20a1 1 0 0 1-1 1A17 17 0 0 1 3 4a1 1 0 0 1 1-1h3.5a1 1 0 0 1 1 1 11.4 11.4 0 0 0 .6 3.6 1 1 0 0 1-.25 1z"/></svg>512-555-0148</span>
  <span><svg width="12" height="12" viewBox="0 0 24 24"><rect x="2" y="5" width="20" height="14" fill="#fff"/><path d="M2 5l10 8 10-8" stroke="#6cbf9c" stroke-width="2" fill="none"/></svg>hello@whitfieldresearch.net</span>
  <a class="cta" href="#">Make an appointment</a>
</div>

<header class="header">
  <div class="brand"><div class="brand-mark"></div><div class="brand-name">Whitfield Research</div></div>
  <nav class="nav">
    <a class="active" href="#">Home</a><a href="#">About</a><a href="#">Services</a><a href="#">Contact</a><a href="#">Publications</a><a href="#">Blog</a><a href="#">Links</a>
  </nav>
</header>

<section class="hero" role="img" aria-label="Photo of a researcher in a lab coat examining a sample">
  <div class="hero-box">
    <h1>Dana Whitfield</h1>
    <h2>Professional Genealogist</h2>
    <p>Careful research into family lines, old records and origins, presented clearly for every client.</p>
    <a class="hero-btn" href="#">Read more</a>
  </div>
</section>

<section class="services">
  <div class="section-title">Our Services</div>
  <div class="section-rule"></div>
  <div class="arrow" style="left:130px;top:240px"><svg width="8" height="10" viewBox="0 0 8 10"><path d="M6 1L2 5l4 4" stroke="#fff" stroke-width="2" fill="none"/></svg></div>
  <div class="arrow" style="right:130px;top:240px"><svg width="8" height="10" viewBox="0 0 8 10"><path d="M2 1l4 4-4 4" stroke="#fff" stroke-width="2" fill="none"/></svg></div>
  <div class="service-list">
    <div class="service">
      <div class="service-icon"><svg width="34" height="34" viewBox="0 0 24 24"><circle cx="10" cy="10" r="6" stroke="#fff" stroke-width="2.4" fill="none"/><path d="M15 15l6 6" stroke="#fff" stroke-width="2.4"/></svg></div>
      <h3>Forensic Genealogy</h3>
      <p>Tracing records and family links with care and clear reports.</p>
    </div>
    <div class="service">
      <div class="service-icon"><svg width="34" height="34" viewBox="0 0 24 24"><rect x="4" y="3" width="16" height="18" rx="2" stroke="#fff" stroke-width="2.2" fill="none"/><path d="M8 9h8M8 13h8M8 17h5" stroke="#fff" stroke-width="2"/></svg></div>
      <h3>Kinship Determination</h3>
      <p>Tracing records and family links with care and clear reports.</p>
    </div>
    <div class="service">
      <div class="service-icon"><svg width="34" height="34" viewBox="0 0 24 24"><circle cx="12" cy="12" r="8" stroke="#fff" stroke-width="2.4" fill="none"/><path d="M12 7v5l3 3" stroke="#fff" stroke-width="2.2" fill="none"/></svg></div>
      <h3>Research Analysis</h3>
      <p>Tracing records and family links with care and clear reports.</p>
    </div>
  </div>
</section>

<section class="work">
  <div class="section-title">Our Work</div>
  <div class="section-rule"></div>
  <div class="work-grid">
    <div class="photo tile-wide" role="img" aria-label="Photo of researchers working with lab samples"></div>
    <div class="photo" role="img" aria-label="Photo of a scientist with test tubes" style="background:linear-gradient(135deg,#d6e3e8,#a9c0ca)"></div>
    <div class="photo" role="img" aria-label="Photo of a team at a lab bench"></div>
    <div class="photo tile-wide" role="img" aria-label="Photo of a researcher holding a flask" style="background:linear-gradient(135deg,#e3ebee,#b4c9d1)"></div>
    <div class="work-feature"><h4>Dolores Voluptatem</h4><a href="#">View More →</a></div>
    <div class="photo" role="img" aria-label="Photo of lab work in progress" style="background:linear-gradient(135deg,#c4d5db,#9fb8c3)"></div>
    <div class="photo" role="img" aria-label="Photo of two researchers discussing results"></div>
    <div class="photo tile-wide" role="img" aria-label="Photo of a researcher at a microscope" style="background:linear-gradient(135deg,#e8eef0,#bccdd3)"></div>
  </div>
</section>

<section class="why">
  <div class="section-title">Why Choose Us</div>
  <div class="why-grid">
    <div class="why-item"><div class="why-num">1</div><div><h5>Asperiatur magni quae</h5><p>Sources checked twice and every finding explained in plain words.</p></div></div>
    <div class="why-item"><div class="why-num">2</div><div><h5>Aperiam aut veritatis beatae</h5><p>Sources checked twice and every finding explained in plain words.</p></div></div>
    <div class="why-item"><div class="why-num">3</div><div><h5>Oluptas aut doloremque</h5><p>Sources checked twice and every finding explained in plain words.</p></div></div>
    <div class="why-item"><div class="why-num">4</div><div><h5>Eaque inventore aut quasi</h5><p>Sources checked twice and every finding explained in plain words.</p></div></div>
    <div class="why-item"><div class="why-num">5</div><div><h5>Doloremque dolores totam</h5><p>Sources checked twice and every finding explained in plain words.</p></div></div>
    <div class="why-item"><div class="why-num">6</div><div><h5>Aut veritatis explicabo</h5><p>Sources checked twice and every finding explained in plain words.</p></div></div>
  </div>
</section>

<section class="team">
  <div class="section-title">Meet Our Team</div>
  <div class="team-list">
    <div class="member">
      <div class="photo" role="img" aria-label="Portrait photo of a team member in a lab coat"></div>
      <div class="member-row"><div><h6>Jhone Doe</h6><small>Research</small></div><div class="dots"><i></i><i></i><i></i></div></div>
    </div>
    <div class="member">
      <div class="photo" role="img" aria-label="Portrait photo of a consultant in a lab coat" style="background:linear-gradient(135deg,#e6edf0,#b8cbd3)"></div>
      <div class="member-row"><div><h6>James Doe</h6><small>Consultant</small></div><div class="dots"><i></i><i></i><i></i></div></div>
    </div>
    <div class="member">
      <div class="photo" role="img" aria-label="Portrait photo of an analyst in a lab coat" style="background:linear-gradient(135deg,#d2dfe4,#a7bec8)"></div>
      <div class="member-row"><div><h6>Alvin Doe</h6><small>Analist</small></div><div class="dots"><i></i><i></i><i></i></div></div>
    </div>
  </div>
</section>

<section class="partners">
  <div class="arrow" style="left:130px;top:89px"><svg width="8" height="10" viewBox="0 0 8 10"><path d="M6 1L2 5l4 4" stroke="#fff" stroke-width="2" fill="none"/></svg></div>
  <div class="partner-list">
    <div class="partner">Northgate<b></b></div>
    <div class="partner">Corvex</div>
    <div class="partner">Lumora</div>
    <div class="partner">Harbor Trust</div>
    <div class="partner"><b></b>Railwise</div>
  </div>
  <div class="arrow" style="right:130px;top:89px"><svg width="8" height="10" viewBox="0 0 8 10"><path d="M2 1l4 4-4 4" stroke="#fff" stroke-width="2" fill="none"/></svg></div>
</section>

<footer class="footer">
  <div>
    <h6>About us</h6>
    <p>Genealogy research for families, lawyers and historians, with clear and honest reporting.</p>
    <a class="more" href="#">Read More →</a>
  </div>
  <div>
    <h6>Address</h6>
    <p>Dana Whitfield<br>Whitfield Research<br>PO Box 4410<br>Austin, TX 78700<br>512-555-0148</p>
    <a class="more" href="#"><svg width="10" height="12" viewBox="0 0 10 12"><path d="M5 0a4 4 0 0 1 4 4c0 3-4 8-4 8S1 7 1 4a4 4 0 0 1 4-4z" fill="#6cbf9c"/></svg> Open in map</a>
  </div>
  <div>
    <h6>Recent tweet</h6>
    <div class="tweet"><i></i>Seven new record sets added to the archive</div>
    <div class="tweet"><i></i>Seven new record sets added to the archive</div>
    <a class="more" href="#">View More →</a>
  </div>
  <div>
    <h6>Contact</h6>
    <p>Send a message and I will reply within two working days.</p>
    <div class="subscribe"><span>Enter your email</span><b>Send</b></div>
  </div>
</footer>

<div class="bottom">
  <span class="copy">© 2024 Dana Whitfield All Rights Reserved</span>
  <a href="#">About us</a><a href="#">Terms and use</a><a href="#">Privacy policy</a><a href="#">FAQs</a><a href="#">Contact us</a>
  <div class="social"><i></i><i></i><i></i><i></i><i></i><i></i></div>
</div>

</body>
</html>
```